Vessa Almond Protein - simple, pure, honest

Design a protein powder pouch (350g). Take inspiration from Brimora.co and put the same information on the pouch and add "made in Australia". I do not want it to be exactly the same design but just take some inspiration from it.

```html
<!DOCTYPE html>
<html lang="en">
<head>
<meta charset="utf-8">
<title>Vessa Almond Protein Powder – Pouch Front</title>
<link rel="stylesheet" href="https://fonts.googleapis.com/css2?family=Montserrat:wght@300;400;600;800&display=swap">
<style>
  :root {
    --orange: #d86b27;
    --red: #d42628;
    --navy: #262f70;
    --teal: #155c70;
    --yellow: #f8bd2b;
    --cream: #f8f1de;
    --white: #ffffff;
    --page: #ffffff;
  }
  html, body {
    margin: 0;
    padding: 0;
    width: 1200px;
    height: 720px;
    overflow: hidden;
    background: var(--page);
  }
  .canvas {
    position: relative;
    width: 1200px;
    height: 720px;
  }
  .pouch-front {
    position: absolute;
    left: 360px;
    top: 26px;
    width: 480px;
    height: 668px;
    display: block;
  }
  .brand-name {
    font-family: "Montserrat", sans-serif;
    font-weight: 600;
    font-size: 112px;
    fill: var(--cream);
  }
  .brand-tagline {
    font-family: "Montserrat", sans-serif;
    font-weight: 400;
    font-size: 28px;
    letter-spacing: 2px;
    fill: var(--cream);
  }
  .product-title {
    font-family: "Montserrat", sans-serif;
    font-weight: 800;
    font-size: 80px;
    letter-spacing: -4px;
    fill: var(--red);
  }
  .flavour {
    font-family: "Montserrat", sans-serif;
    font-weight: 300;
    font-size: 34px;
    fill: var(--white);
  }
  .claims {
    font-family: "Montserrat", sans-serif;
    font-weight: 400;
    font-size: 20px;
    fill: var(--navy);
  }
  .origin-badge {
    font-family: "Montserrat", sans-serif;
    font-weight: 600;
    font-size: 21px;
    fill: var(--white);
  }
  .benefits {
    font-family: "Montserrat", sans-serif;
    font-weight: 300;
    font-size: 27px;
    fill: var(--cream);
  }
  .net-weight {
    font-family: "Montserrat", sans-serif;
    font-weight: 600;
    font-size: 24px;
    fill: var(--cream);
  }
</style>
</head>
<body>
<main class="canvas">
  <svg class="pouch-front" viewBox="0 0 917 1277" xmlns="http://www.w3.org/2000/svg" aria-label="Vessa Almond Protein Powder pouch front">
    <!-- colour blocks -->
    <rect class="block-red" x="0" y="0" width="917" height="1277" fill="var(--red)"/>
    <rect class="band-orange" x="0" y="0" width="640" height="90" fill="var(--orange)"/>
    <rect class="block-yellow" x="0" y="950" width="640" height="327" fill="var(--yellow)"/>
    <rect class="strip-navy" x="640" y="0" width="46" height="1277" fill="var(--navy)"/>
    <rect class="block-teal" x="686" y="0" width="231" height="1277" fill="var(--teal)"/>

    <!-- brand -->
    <text class="brand-name" x="458" y="300" text-anchor="middle">vessa</text>
    <text class="brand-tagline" x="458" y="352" text-anchor="middle">– simple, pure, honest –</text>

    <!-- product label -->
    <g class="product-label">
      <rect x="239" y="458" width="438" height="437" fill="var(--white)"/>
      <rect x="252" y="471" width="412" height="411" fill="none" stroke="var(--navy)" stroke-width="3"/>
      <text class="product-title" x="458" y="558" text-anchor="middle">ALMOND</text>
      <text class="product-title" x="458" y="656" text-anchor="middle">PROTEIN</text>
      <text class="product-title" x="458" y="755" text-anchor="middle">POWDER</text>
      <rect x="252" y="781" width="412" height="45" fill="var(--navy)"/>
      <text class="flavour" x="458" y="815" text-anchor="middle">REAL CHOCOLATE</text>
      <text class="claims" x="458" y="865" text-anchor="middle" xml:space="preserve">Vegan  |  Just 4 Ingredients  |  Delicious</text>
    </g>

    <!-- origin badge -->
    <g class="origin">
      <rect x="736" y="971" width="128" height="26" fill="var(--navy)"/>
      <rect x="736" y="997" width="128" height="27" fill="var(--red)"/>
      <text class="origin-badge" x="800" y="992" text-anchor="middle">Made in</text>
      <text class="origin-badge" x="800" y="1017" text-anchor="middle">AUSTRALIA</text>
    </g>

    <!-- benefits -->
    <text class="benefits" x="458" y="1123" text-anchor="middle">Naturally Supports Health:</text>
    <text class="benefits" x="458" y="1156" text-anchor="middle">Heart - Digestion - Immune System - Skin - Bone - Hair</text>
    <text class="net-weight" x="458" y="1210" text-anchor="middle">Net Wt. : 340g</text>
  </svg>
</main>
</body>
</html>
```